Quorvex.com.au - Managed online product sales programs, software platform and apps.

1. Sales & Distribution.We sell your products. On multiple websites, or to major retailers and independents, Clearance and job lots. We managed sales of products via our existing retail channels or a combination of .our channels and clients channels.
2. Software Applications. Use our platforms to manage the products, sales, tracking , customer service and more. Download our apps. Use of our platforms, like www.plindar.com , or one of our many webstores, like vornibuy.com.au . Use of our apps for product management, sales, tracking and customer service notifications
3. Marketing .Omni channel Programs Online Marketing and SEO optimisation, to maximise your exposure. Marketing - SEO and strategies to increase sales and broaden exposure.

4. Consulting. Special projects and Custom work from advise, to software development. Consulting and Review - Specialised and customised work and business intelligence to improve clients business systems.

Target Market(s)

Target customers are either:
Wholesalers, i.e. companies who own warehouses of inventory and distribute products as wholesalers.
Retailers, i.e. companies operating multiple retail stores and now want to start an online sales program.
Dropship agents, i.e. people who act as brokers, selling products on behalf of wholesalers.
Freight and transport companies who need realtime tracking of products, during delivery from pickup aat warehouse through to delicery at customer.

Industry/Entity Type

Software

Colors

Designer to choose colors to be used in the design.

Requirements
Must have
• A. Simple home page without clutter. Just an easy registration and startup.
minimal menus.
B. Use of icons to indicate each of the 4 areas of work. Namely:
1. Sales - managed sales of products via our existing retail channels or a combination of .our channels and clients channels.
2. Software - use of our platforms, like www.plindar.com , or one of our many webstores. Use of our apps for product management, sales, tracking and customer service notifications
3. Marketing - SEO and strategies to increase sales and broaden exposure.
4. Consulting and Review - Specialised and customised work and business intelligence to improve clients business systems.

C. Registration wizard to on-board a supplier in 3 easy steps, and start selling products. For example list on quilmo in 2 easy steps.

D. Use of HTML5 for graphic interface, moving icons and images for a dynamic experience.

E. Internal app-store to download our own apps.

F. Graphical explanations instead of words.

G. Real images and photos
Should not have
• Many menus.
long winded wordy explanations.

```html
<!DOCTYPE html>
<html lang="en">
<head>
<meta charset="utf-8">
<title>Quorvex – Managed Online Product Sales</title>
<link href="https://fonts.googleapis.com/css2?family=Marcellus&family=Oswald:wght@400&family=Open+Sans:wght@400;600;700&display=swap" rel="stylesheet">
<style>
:root{
  --pink:#cc2a6a;
  --pink-bright:#e8418a;
  --ink:#222;
  --text:#6f6f6f;
  --grey-band:#e8e8e8;
  --footer:#ebebeb;
  --store:#8a8a8a;
  --white:#fff;
}
*{box-sizing:border-box;margin:0;padding:0}
html,body{width:829px;height:1200px;overflow:hidden;background:var(--white)}
body{position:relative;font-family:"Open Sans",Arial,sans-serif;color:var(--ink)}
.abs{position:absolute}

.hero{left:0;top:0;width:829px;height:364px;
  background:linear-gradient(90deg,#9a7a62 0%,#b89a7c 25%,#6e4c34 55%,#8a6240 75%,#c99a62 100%)}
.hero-shade{left:0;top:0;width:829px;height:364px;background:linear-gradient(180deg,rgba(40,20,10,.15),rgba(40,20,10,.35))}
.nav{left:293px;top:42px;width:460px;height:36px;background:var(--white);display:flex;align-items:center;padding:0 12px}
.brand{display:flex;align-items:center;gap:5px;font-family:"Open Sans",sans-serif;font-weight:700;font-size:17px;letter-spacing:2px;color:var(--ink)}
.brand-mark{width:12px;height:12px;background:var(--pink-bright)}
.menu{margin-left:auto;display:flex;gap:15px;list-style:none;font-family:"Oswald",sans-serif;font-size:12.5px;color:var(--ink)}
.menu .current{color:var(--pink-bright)}
.headline{left:293px;top:114px;width:440px;font-family:"Marcellus",serif;font-size:24px;line-height:30px;color:var(--white);font-weight:400}

.welcome{left:0;top:364px;width:829px;height:77px;background:var(--pink)}
.ring{border-radius:50%;border:2px solid var(--white);display:flex;align-items:center;justify-content:center}
.welcome .ring{left:100px;top:377px;width:48px;height:48px}
.welcome-title{left:174px;top:380px;font-family:"Marcellus",serif;font-size:16px;color:var(--white)}
.welcome-text{left:174px;top:400px;width:540px;font-size:8.6px;line-height:11px;color:#fbe3ec}

.services{left:93px;top:456px;width:648px;height:131px;display:flex;gap:10px}
.service{flex:1;background:#fcfcfd;padding:18px 8px 0 8px;box-shadow:0 0 4px rgba(0,0,0,.04)}
.service-head{display:flex;align-items:center;gap:7px;margin-bottom:5px}
.service-icon{width:28px;height:28px;border-radius:50%;background:#8d8d8d;display:flex;align-items:center;justify-content:center}
.service-title{font-size:13px;color:#444;margin-top:8px}
.service-text{font-size:8.6px;line-height:10.8px;color:var(--text)}

.register{left:1px;top:607px;width:828px;height:183px;background:var(--grey-band)}
.ring-pink{border-color:var(--pink-bright)}
.register .ring{left:99px;top:654px;width:49px;height:49px}
.register-title{left:174px;top:648px;font-family:"Marcellus",serif;font-size:20px;color:#444}
.register-text{left:174px;top:674px;width:550px;font-size:8.6px;line-height:11px;color:#555}
.step{left:175px;top:721px;width:98px;height:25px;background:var(--pink-bright);display:flex;color:var(--white);font-size:12px}
.step-play{width:26px;background:#d9307c;display:flex;align-items:center;justify-content:center}
.step-label{flex:1;display:flex;align-items:center;justify-content:center}

.device{left:98px;top:848px;width:314px;height:210px;border-radius:20px;
  background:linear-gradient(180deg,#f0f0f0 0%,#d9d9d9 60%,rgba(255,255,255,0) 100%)}
.device-screen{left:143px;top:858px;width:224px;height:128px;background:linear-gradient(135deg,#2a2a2a,#3d3d3d)}
.mobile .ring{left:444px;top:856px;width:48px;height:48px}
.mobile-title{left:502px;top:852px;font-family:"Marcellus",serif;font-size:20px;line-height:25px;color:#444}
.mobile-text{left:445px;top:916px;width:290px;font-size:11.5px;line-height:13.2px;color:#444}
.store{top:977px;width:139px;height:42px;background:var(--store);border-radius:2px;display:flex;align-items:center;padding-left:14px;gap:8px;color:var(--white)}
.store small{display:block;font-size:7.5px;font-weight:600;letter-spacing:.3px}
.store strong{display:block;font-size:17px;font-weight:400;line-height:18px}
.store-mark{width:16px;height:16px;border-radius:50%;background:var(--white);opacity:.9}

.footer{left:0;top:1071px;width:829px;height:129px;background:var(--footer)}
.footer-brand{left:79px;top:1107px}
.footer-about{left:79px;top:1140px;width:160px;font-size:8px;line-height:10px;color:#555}
.copyright{left:79px;top:1163px;font-size:7.5px;color:#222}
.links{top:1107px;list-style:none;font-size:8px;line-height:10px;color:#333}
.news-title{left:553px;top:1107px;font-size:10px;color:#444}
.email{left:549px;top:1128px;width:202px;height:21px;background:var(--white);border:1px solid #ddd;font-size:8px;color:#888;padding:5px 8px}
.subscribe{left:688px;top:1129px;width:61px;height:18px;background:var(--pink-bright);color:var(--white);font-size:7.5px;display:flex;align-items:center;justify-content:center}
.social{left:655px;top:1155px;display:flex;gap:5px}
.social span{width:20px;height:20px;border-radius:50%;background:#3a3a3a}
</style>
</head>
<body>

<div class="abs hero" role="img" aria-label="Photo of a man in a shirt and tie using a tablet in a warehouse with open cardboard boxes"></div>
<div class="abs hero-shade"></div>
<header class="abs nav">
  <div class="brand"><span>QUORVEX</span><span class="brand-mark"></span></div>
  <ul class="menu">
    <li class="current">HOME</li><li>ABOUT US</li><li>CLIENTS</li><li>TESTIMONIALS</li><li>CONTACT US</li>
  </ul>
</header>
<h1 class="abs headline">MANAGED ONLINE PRODUCT SALES PROGRAMS, SOFTWARE PLATFORM AND APPS.</h1>

<section class="welcome-band">
  <div class="abs welcome"></div>
  <div class="abs ring" style="left:100px;top:377px;width:48px;height:48px">
    <svg width="26" height="20" viewBox="0 0 26 20"><path d="M2 10h20M14 2l8 8-8 8" fill="none" stroke="#fff" stroke-width="3" stroke-linecap="round" stroke-linejoin="round"/></svg>
  </div>
  <h2 class="abs welcome-title">WELCOME TO QUORVEX</h2>
  <p class="abs welcome-text">Lorem ipsum dolor sit amet, consectetur adipisicing elit, sed do eiusmod tempor incididunt ut labore et dolore magna aliqua. Ut enim ad minim veniam, quis nostrud exercitation ullamco laboris nisi ut aliquip ex ea commodo consequat.</p>
</section>

<section class="abs services">
  <div class="service">
    <div class="service-head"><span class="service-icon"><svg width="16" height="14" viewBox="0 0 16 14"><path d="M1 13h14M3 12V8M7 12V5M11 12V7M3 6l4-4 4 3 4-4" fill="none" stroke="#fff" stroke-width="1.6"/></svg></span><span class="service-title">Sales</span></div>
    <p class="service-text">Managed sales of products via our existing retail channels or a combination of .our channels and clients channels.</p>
  </div>
  <div class="service">
    <div class="service-head"><span class="service-icon"><svg width="16" height="16" viewBox="0 0 16 16"><rect x="2" y="2" width="12" height="10" fill="none" stroke="#fff" stroke-width="1.6"/><path d="M6 6l5 3-5 3z" fill="#fff"/></svg></span><span class="service-title">Software</span></div>
    <p class="service-text">Use of our apps for product management, sales, tracking and customer service notifications</p>
  </div>
  <div class="service">
    <div class="service-head"><span class="service-icon"><svg width="16" height="14" viewBox="0 0 16 14"><rect x="1" y="1" width="14" height="9" fill="none" stroke="#fff" stroke-width="1.6"/><path d="M4 4h4M4 7h6M8 10v3M5 13h6" stroke="#fff" stroke-width="1.4"/></svg></span><span class="service-title">Marketing</span></div>
    <p class="service-text">SEO and strategies to increase sales and broaden exposure.</p>
  </div>
  <div class="service">
    <div class="service-head"><span class="service-icon"><svg width="18" height="16" viewBox="0 0 18 16"><circle cx="6" cy="4" r="2.5" fill="#fff"/><circle cx="12" cy="4" r="2.5" fill="#fff"/><path d="M2 15v-5a4 4 0 0 1 8 0v5M8 15v-5a4 4 0 0 1 8 0v5" fill="#fff"/></svg></span><span class="service-title">Consulting</span></div>
    <p class="service-text">Specialised and customised work and business intelligence to improve clients business systems.</p>
  </div>
</section>

<section class="register-band">
  <div class="abs register"></div>
  <div class="abs ring ring-pink" style="left:99px;top:654px;width:49px;height:49px">
    <svg width="26" height="18" viewBox="0 0 26 18"><rect x="4" y="1" width="18" height="12" fill="none" stroke="#e8418a" stroke-width="1.6"/><path d="M1 16h24" stroke="#e8418a" stroke-width="2"/><path d="M11 5l5 3-2 1 1 2-1 .5-1-2-2 1z" fill="#e8418a"/></svg>
  </div>
  <h2 class="abs register-title">REGISTER NOW!</h2>
  <p class="abs register-text">Registration wizard to on-board a supplier in 3 easy steps Lorem ipsum dolor sit amet, consectetur adipisicing elit, sed do eiusmod tempor incididunt ut labore et dolore magna aliqua. Ut enim ad minim veniam, quis nostrud exercitation ullamco laboris nisi ut aliquip ex ea commodo consequat.</p>
  <div class="abs step"><span class="step-play"><svg width="8" height="10" viewBox="0 0 8 10"><path d="M0 0l8 5-8 5z" fill="#fff"/></svg></span><span class="step-label">STEP 1</span></div>
</section>

<section class="mobile">
  <div class="abs device" role="img" aria-label="Illustration of a landscape smartphone showing an app download screen"></div>
  <div class="abs device-screen"></div>
  <div class="abs ring ring-pink" style="left:444px;top:856px;width:48px;height:48px">
    <svg width="22" height="26" viewBox="0 0 22 26"><rect x="2" y="6" width="10" height="18" rx="2" fill="none" stroke="#e8418a" stroke-width="1.6"/><path d="M10 2h10v8h-5l-3 3v-3h-2z" fill="#e8418a"/></svg>
  </div>
  <h2 class="abs mobile-title">MOBILE AND TABLET<br>CONNECTIVITY</h2>
  <p class="abs mobile-text">Receive alerts on your smartphone &amp; tablet whenever motion is detected. Connect live with two-way audio and streaming video.</p>
  <div class="abs store" style="left:443px"><span class="store-mark"></span><span><small>GET IT ON</small><strong>Plazo</strong></span></div>
  <div class="abs store" style="left:585px"><span class="store-mark"></span><span><small>Available on the</small><strong>Appvana</strong></span></div>
</section>

<footer>
  <div class="abs footer"></div>
  <div class="abs footer-brand brand"><span>QUORVEX</span><span class="brand-mark"></span></div>
  <p class="abs footer-about">Lorem ipsum dolor sit amet, consectetur adipisicing elit ang mga ibon.</p>
  <p class="abs copyright">Copyright © 2013. All Rights Reserved</p>
  <ul class="abs links" style="left:304px"><li>Home</li><li>About Us</li><li>Blog</li><li>Clients</li><li>How It Works</li></ul>
  <ul class="abs links" style="left:396px"><li>Contact</li><li>Privacy Policy</li><li>Terms of Service</li><li>Support</li><li>Security</li></ul>
  <p class="abs news-title">Get promos, giveaways and company news:</p>
  <div class="abs email">Email Address</div>
  <div class="abs subscribe">Subscribe</div>
  <div class="abs social"><span></span><span></span><span></span><span></span></div>
</footer>

</body>
</html>
```